Retail healthy snack bar design

We are launching a new product range to be sold in health food stores.

The Vorla Co (no logo as yet).

We will have a range of bars, spreads (jars), shakes (bags) in the following ranges-
milk protein
plant protein
keto

For this project, please do a bar design. The chosen designer will be given additional work for the rest of the packaging as well as promotional material such as social media, banners, posters etc.

Brisk Stick Protein - Must be White to be recognized.
Brisk Stick Collagen - Bronze
Brisk Keto Stick - Possibly Red
Brisk Stick Plant - Green

Food images can be added but their must be samples without as we may need to remove for certain countries.

Target Market(s)

Healthy, Weight-loss, Bodybuilding, Elderly, Medical

Industry/Entity Type

Health And Wellness

Font styles to use
Sans Serif

Colors

Designer to choose colors to be used in the design.

Requirements
Must have
• Clean simple to read design with minimal colours

Flavour to be easily read (Must include the word 'Flavour' in the same size font as the flavour description)

Must show size of bar (60g).

Some details that can be added (optional)-
raw, cold pressed bar with (example) whey protein isolate + prebiotic fibre
natural, with no artificial colours, flavours, preservatives or sweeteners
no added sugar or sugar alcohols - gluten free - soy free

Rear of bar shall remain the same or all same details if redesigned.
Nice to have
• Clean design, use of silver foil and/or matt/gloss affect, large oversized flavour image (if including).

See images of current designs I like on the market for ideas
Should not have
• Too many images (if any).

```html
<!DOCTYPE html>
<html lang="en">
<head>
<meta charset="utf-8">
<title>Brisk Stick bar range</title>
<link rel="stylesheet" href="https://fonts.googleapis.com/css2?family=Open+Sans:wght@400;600;800&display=swap">
<style>
  :root {
    --stage: #3b3b3d;
    --navy: #0b1a8a;
    --royal: #1f4ee6;
    --sun: #ffdc14;
    --white: #ffffff;
    --silver: #e4e6ea;
    --silver-dark: #c3c7cd;
    --leaf: #1f9a1f;
    --leaf-light: #3cc43c;
    --lime: #78c83c;
    --tang: #ff5a0a;
    --aqua: #38e6f0;
    --ink: #111111;
  }
  html, body {
    margin: 0;
    width: 1200px;
    height: 857px;
    overflow: hidden;
    background: var(--stage);
    font-family: "Open Sans", sans-serif;
  }
  .range {
    position: relative;
    width: 1200px;
    height: 857px;
  }
  .wrapper {
    position: absolute;
    width: 560px;
    height: 200px;
    transform: rotate(-32deg);
  }
  .wrapper--protein-blue  { left: 6px;   top: 185px; }
  .wrapper--protein-white { left: 28px;  top: 465px; }
  .wrapper--plant         { left: 548px; top: 168px; }
  .wrapper--protein-silver{ left: 554px; top: 454px; }

  .crimp-shade { fill: #000; opacity: .12; }
  .crimp-light { fill: #fff; opacity: .25; }
  .brand-name {
    font-family: "Open Sans", sans-serif;
    font-weight: 800;
    font-size: 40px;
  }
  .range-name {
    font-family: "Open Sans", sans-serif;
    font-weight: 800;
    font-size: 22px;
    letter-spacing: 9px;
  }
  .flavour {
    font-family: "Open Sans", sans-serif;
    font-weight: 600;
    font-size: 15px;
  }
  .weight {
    font-family: "Open Sans", sans-serif;
    font-weight: 400;
    font-size: 17px;
    fill: var(--ink);
  }
  .claims {
    font-family: "Open Sans", sans-serif;
    font-weight: 400;
    font-size: 10px;
  }
</style>
</head>
<body>
<main class="range">

  <!-- Protein, blue -->
  <svg class="wrapper wrapper--protein-blue" viewBox="0 0 560 200" aria-label="Brisk Stick Protein vanilla flavour bar, blue">
    <defs>
      <clipPath id="shape-a"><polygon points="20,0 0,10 20,20 0,30 20,40 0,50 20,60 0,70 20,80 0,90 20,100 0,110 20,120 0,130 20,140 0,150 20,160 0,170 20,180 0,190 20,200 540,200 560,190 540,180 560,170 540,160 560,150 540,140 560,130 540,120 560,110 540,100 560,90 540,80 560,70 540,60 560,50 540,40 560,30 540,20 560,10 540,0"/></clipPath>
    </defs>
    <g clip-path="url(#shape-a)">
      <rect width="560" height="200" style="fill:var(--navy)"/>
      <rect width="200" height="200" style="fill:var(--royal)"/>
      <circle cx="475" cy="10" r="85" style="fill:var(--sun)"/>
      <rect x="0" width="52" height="200" class="crimp-shade"/>
      <rect x="508" width="52" height="200" class="crimp-shade"/>
    </g>
    <text class="flavour" x="470" y="22" text-anchor="middle" style="fill:var(--ink)">VANILA</text>
    <text class="flavour" x="470" y="40" text-anchor="middle" style="fill:var(--ink)">FLAVOUR</text>
    <circle cx="470" cy="128" r="23" style="fill:var(--white)"/>
    <text class="weight" x="470" y="134" text-anchor="middle">60g</text>
    <text class="brand-name" x="95" y="100" style="fill:var(--tang)">Brisk Stick</text>
    <text class="range-name" x="150" y="140" style="fill:var(--white)">PROTEIN</text>
    <text class="claims" x="70" y="190" style="fill:var(--white)">no added sugar, sugar alcohols, gluten free, soy free</text>
  </svg>

  <!-- Protein, white -->
  <svg class="wrapper wrapper--protein-white" viewBox="0 0 560 200" aria-label="Brisk Stick Protein vanilla flavour bar, white">
    <defs>
      <clipPath id="shape-b"><polygon points="20,0 0,10 20,20 0,30 20,40 0,50 20,60 0,70 20,80 0,90 20,100 0,110 20,120 0,130 20,140 0,150 20,160 0,170 20,180 0,190 20,200 540,200 560,190 540,180 560,170 540,160 560,150 540,140 560,130 540,120 560,110 540,100 560,90 540,80 560,70 540,60 560,50 540,40 560,30 540,20 560,10 540,0"/></clipPath>
    </defs>
    <g clip-path="url(#shape-b)">
      <rect width="560" height="200" style="fill:var(--white)"/>
      <polygon points="0,150 110,150 80,175 0,175" style="fill:var(--sun)"/>
      <polygon points="150,20 190,20 160,60" style="fill:var(--lime)"/>
      <circle cx="475" cy="10" r="85" style="fill:var(--sun)"/>
      <rect x="0" width="52" height="200" style="fill:var(--silver)" opacity=".6"/>
      <rect x="508" width="52" height="200" style="fill:var(--silver)" opacity=".6"/>
    </g>
    <text class="flavour" x="470" y="22" text-anchor="middle" style="fill:var(--ink)">VANILA</text>
    <text class="flavour" x="470" y="40" text-anchor="middle" style="fill:var(--ink)">FLAVOUR</text>
    <circle cx="470" cy="128" r="23" style="fill:var(--white);stroke:var(--ink);stroke-width:1"/>
    <text class="weight" x="470" y="134" text-anchor="middle">60g</text>
    <text class="brand-name" x="95" y="100" style="fill:var(--royal)">Brisk Stick</text>
    <text class="range-name" x="150" y="140" style="fill:var(--lime)">PROTEIN</text>
    <text class="claims" x="70" y="190" style="fill:var(--ink)">no added sugar, sugar alcohols, gluten free, soy free</text>
  </svg>

  <!-- Plant, green -->
  <svg class="wrapper wrapper--plant" viewBox="0 0 560 200" aria-label="Brisk Stick Plant vanilla flavour bar, green">
    <defs>
      <clipPath id="shape-c"><polygon points="20,0 0,10 20,20 0,30 20,40 0,50 20,60 0,70 20,80 0,90 20,100 0,110 20,120 0,130 20,140 0,150 20,160 0,170 20,180 0,190 20,200 540,200 560,190 540,180 560,170 540,160 560,150 540,140 560,130 540,120 560,110 540,100 560,90 540,80 560,70 540,60 560,50 540,40 560,30 540,20 560,10 540,0"/></clipPath>
    </defs>
    <g clip-path="url(#shape-c)">
      <rect width="560" height="200" style="fill:var(--leaf)"/>
      <path d="M60,40 C160,10 260,60 330,20 L330,200 L60,200 Z" style="fill:var(--leaf-light)" opacity=".5"/>
      <polygon points="420,0 560,0 560,200 520,200" style="fill:var(--sun)"/>
      <polygon points="400,0 425,0 525,200 505,200" style="fill:var(--tang)"/>
      <polygon points="385,0 398,0 503,200 492,200" style="fill:var(--white)"/>
      <rect x="0" width="52" height="200" class="crimp-shade"/>
      <rect x="508" width="52" height="200" class="crimp-shade"/>
    </g>
    <text class="flavour" x="490" y="22" text-anchor="middle" style="fill:var(--ink)">VANILA</text>
    <text class="flavour" x="490" y="40" text-anchor="middle" style="fill:var(--ink)">FLAVOUR</text>
    <circle cx="440" cy="138" r="23" style="fill:var(--white)"/>
    <text class="weight" x="440" y="144" text-anchor="middle">60g</text>
    <text class="brand-name" x="95" y="100" style="fill:var(--tang)">Brisk Stick</text>
    <text class="range-name" x="165" y="140" style="fill:var(--sun)">PLANT</text>
    <text class="claims" x="70" y="190" style="fill:var(--white)">no added sugar, sugar alcohols, gluten free, soy free</text>
  </svg>

  <!-- Protein, silver -->
  <svg class="wrapper wrapper--protein-silver" viewBox="0 0 560 200" aria-label="Brisk Stick Protein vanilla flavour bar, silver">
    <defs>
      <clipPath id="shape-d"><polygon points="20,0 0,10 20,20 0,30 20,40 0,50 20,60 0,70 20,80 0,90 20,100 0,110 20,120 0,130 20,140 0,150 20,160 0,170 20,180 0,190 20,200 540,200 560,190 540,180 560,170 540,160 560,150 540,140 560,130 540,120 560,110 540,100 560,90 540,80 560,70 540,60 560,50 540,40 560,30 540,20 560,10 540,0"/></clipPath>
      <linearGradient id="foil" x1="0" y1="0" x2="0" y2="1">
        <stop offset="0" stop-color="#f4f5f7"/>
        <stop offset=".5" stop-color="#dadde2"/>
        <stop offset="1" stop-color="#f0f1f3"/>
      </linearGradient>
    </defs>
    <g clip-path="url(#shape-d)">
      <rect width="560" height="200" fill="url(#foil)"/>
      <polygon points="420,0 560,0 560,200 520,200" style="fill:var(--royal)"/>
      <polygon points="400,0 425,0 525,200 505,200" style="fill:var(--tang)"/>
      <polygon points="385,0 398,0 503,200 492,200" style="fill:var(--aqua)"/>
      <rect x="0" width="52" height="200" style="fill:var(--silver-dark)" opacity=".5"/>
      <rect x="508" width="52" height="200" style="fill:var(--silver-dark)" opacity=".3"/>
    </g>
    <text class="flavour" x="490" y="22" text-anchor="middle" style="fill:var(--white)">VANILA</text>
    <text class="flavour" x="490" y="40" text-anchor="middle" style="fill:var(--white)">FLAVOUR</text>
    <circle cx="440" cy="138" r="23" style="fill:var(--white);stroke:var(--ink);stroke-width:1"/>
    <text class="weight" x="440" y="144" text-anchor="middle">60g</text>
    <text class="brand-name" x="95" y="100" style="fill:var(--tang)">Brisk Stick</text>
    <text class="range-name" x="150" y="140" style="fill:var(--royal)">PROTEIN</text>
    <text class="claims" x="70" y="190" style="fill:var(--ink)">no added sugar, sugar alcohols, gluten free, soy free</text>
  </svg>

</main>
</body>
</html>
```